Quorvale Harmony Network / Real People/Real Passion/Real Purpose

I am wanting a Website Banner that is Spiritually Inspired, but also relates to everyday people as well / community and nature.
Colours of Orange and green's.
I would have my photo in the top corner and some flow to the banner with small relevant picture's underneath (if necessary I can order these from photo stock) or use a couple of my own, example of website for inspiration is brivantelmistway.co.
and I like the colours on this page.

Reason: It is very important to have the right look and feeling to capture the true essence of what the website is all about... If necessary I will upgrade or send further examples of the type of look I am after if necessary..( I have seen really good banners that you can order through plinthra.com ...but I thought I would have a more professional look if I chose Vantor Lumo to whom I was recommended.. Thankyou

Target Market(s)

Between 35 -65 Spiritually Minded / Health Conscious / Community focussed
concerned about environment.

Industry/Entity Type

Community

Requirements
Must have
• Colours of Orange / Apricot / Peach/ Green / Nature Colours and Flow
Nice to have
• Mostly stated in the description, however if you need more than that please email me. I have not had any luck with a logo so far and have paid out money with no 100% back...so it is on hold for now...so I would like to put my picture on probably the left hand side of the header.
I have a Wordpress site and the banner header would be 1000 x 288. Thankyou

```html
<!DOCTYPE html>
<html lang="en">
<head>
<meta charset="utf-8">
<title>Quorvale Harmony Network – Header Banner</title>
<link rel="stylesheet" href="https://fonts.googleapis.com/css2?family=Arimo:wght@700&family=Pinyon+Script&display=swap">
<style>
  :root {
    --sky-blue: #4a9fc8;
    --sky-teal: #7fb6c4;
    --sunset-gold: #ffd24a;
    --sunset-orange: #f0a030;
    --dusk-rose: #b87a88;
    --dusk-violet: #4a3a78;
    --night-indigo: #2a2458;
    --photo-apricot: #e0a860;
    --photo-ring: #ffffff;
    --ink: #111111;
  }
  html, body {
    margin: 0;
    padding: 0;
    overflow: hidden;
    background: #ffffff;
  }
  .banner {
    position: relative;
    width: 1200px;
    height: 274px;
    overflow: hidden;
  }
  .banner__scenery {
    position: absolute;
    inset: 0;
    background:
      radial-gradient(ellipse 260px 120px at 890px 175px, rgba(255,240,150,0.95), rgba(255,200,60,0.55) 45%, rgba(255,170,40,0) 100%),
      radial-gradient(ellipse 700px 140px at 760px 150px, rgba(250,190,70,0.75), rgba(240,160,60,0) 100%),
      linear-gradient(180deg,
        var(--sky-blue) 0%,
        var(--sky-teal) 22%,
        #c9b98a 42%,
        var(--sunset-orange) 56%,
        var(--dusk-rose) 70%,
        var(--dusk-violet) 84%,
        var(--night-indigo) 100%);
  }
  .portrait-slot {
    position: absolute;
    left: 58px;
    top: -62px;
    width: 302px;
    height: 302px;
    box-sizing: border-box;
    border-radius: 50%;
    background: var(--photo-apricot);
    border: 4px solid var(--photo-ring);
  }
  .portrait-slot__label {
    position: absolute;
    left: 102px;
    top: 58px;
    margin: 0;
    font-family: "Arimo", Arial, sans-serif;
    font-weight: 700;
    font-size: 31px;
    line-height: 42px;
    color: var(--ink);
  }
  .banner__caption {
    position: absolute;
    left: 412px;
    top: 112px;
    margin: 0;
    font-family: "Pinyon Script", cursive;
    font-size: 40px;
    line-height: 1;
    color: var(--ink);
    white-space: nowrap;
    transform: rotate(-7.5deg);
    transform-origin: left center;
  }
</style>
</head>
<body>
  <header class="banner">
    <div class="banner__scenery" role="img" aria-label="Sunset sky over the sea with a lighthouse silhouetted on the right"></div>
    <div class="portrait-slot"></div>
    <p class="portrait-slot__label">Space for<br>your photo</p>
    <p class="banner__caption">Caption will come here</p>
  </header>
</body>
</html>
```